Business Card Design Project

Business card design based on the existing logo.

Target Market(s)

Small to medium business owners and CIO's looking for professional IT services.

Industry/Entity Type

Business

Font styles to use
Serif
Sans Serif

Requirements
Must have
• Logo, company name, company details

Text to appear on the business card
Name / Title:
Leon Fairholt
CEO

Address:
Valtiro Limited
Level 3, 42 Kestle St
P O Box 462
Paraparaumu 5391

Other details:
leon@valtiro.co
Ph: 0800 519 308
Mob: +64 21 948 216
www.valtiro.co

Nice to have
• I would look at both single and double sided options. My initial thought is double sided with just the logo with the grey framing for the front and the name and details on the back. But I'm open to other design options.

```html
<!DOCTYPE html>
<html lang="en">
<head>
<meta charset="utf-8">
<title>Valtiro business card</title>
<link rel="stylesheet" href="https://fonts.googleapis.com/css2?family=Open+Sans:wght@400;600;700&display=swap">
<style>
  :root {
    --brand-blue: #1a6480;
    --ink: #1c1c1c;
    --frame-grey: #a9a9ab;
    --paper: #ffffff;
    --backdrop: #e6e6ea;
    --rule: #b8b8b8;
  }
  * { box-sizing: border-box; margin: 0; padding: 0; }
  html, body {
    width: 1200px; height: 987px; overflow: hidden;
    background: var(--backdrop);
    font-family: "Open Sans", Arial, sans-serif;
  }
  .sheet { position: relative; width: 1200px; height: 987px; }
  .card {
    position: absolute; left: 240px; width: 720px; height: 440px;
    background: var(--paper); border-radius: 26px; overflow: hidden;
  }
  .card--back { top: 33px; }
  .card--front {
    top: 513px;
    border: 14px solid var(--frame-grey);
    display: flex; align-items: center; justify-content: center;
  }
  .swoosh { position: absolute; inset: 0; width: 720px; height: 440px; }
  .wordmark {
    position: relative;
    display: flex; align-items: center; gap: 16px;
    color: var(--ink); font-weight: 600; letter-spacing: -1px; line-height: 1;
  }
  .wordmark__square { background: var(--brand-blue); flex: none; }
  .card--back .wordmark { position: absolute; left: 42px; top: 122px; font-size: 56px; }
  .card--back .wordmark__square { width: 46px; height: 46px; }
  .card--front .wordmark { font-size: 112px; gap: 28px; }
  .card--front .wordmark__square { width: 92px; height: 92px; }
  .contact-list {
    position: absolute; left: 42px; top: 250px; list-style: none;
    font-size: 15px; color: var(--ink); line-height: 24px;
  }
  .contact-list li { display: flex; align-items: center; gap: 9px; }
  .contact-list svg { width: 14px; height: 14px; flex: none; }
  .divider {
    position: absolute; left: 222px; top: 252px; width: 1px; height: 92px;
    background: var(--rule);
  }
  .address {
    position: absolute; left: 238px; top: 254px; font-style: normal;
    font-size: 14px; line-height: 22px; color: var(--ink);
  }
  .person {
    position: absolute; right: 30px; top: 258px; text-align: right; color: var(--paper);
  }
  .person__name { font-size: 24px; font-weight: 700; letter-spacing: .5px; line-height: 1.2; }
  .person__role { font-size: 18px; font-weight: 400; margin-top: 2px; }
</style>
</head>
<body>
<main class="sheet">
  <section class="card card--back" aria-label="Card back with contact details">
    <svg class="swoosh" viewBox="0 0 720 440" aria-hidden="true">
      <path d="M0,0 H720 V440 H580 C438,60 250,0 0,0 Z" fill="var(--brand-blue)"/>
      <path d="M0,16 C240,16 420,62 560,440" fill="none" stroke="#000" stroke-width="7"/>
    </svg>
    <div class="wordmark"><span class="wordmark__square"></span>Valtiro</div>
    <ul class="contact-list">
      <li><svg viewBox="0 0 14 14"><circle cx="7" cy="7" r="7" fill="var(--brand-blue)"/><path d="M4.5 3.5l1.5 1.5-1 1a5 5 0 0 0 3 3l1-1 1.5 1.5-1 1.2C6.5 10.5 3.5 7.5 3.3 4.5z" fill="#fff"/></svg>0800 519 308</li>
      <li><svg viewBox="0 0 14 14"><rect x="3.5" y="1" width="7" height="12" rx="1.5" fill="var(--brand-blue)"/><rect x="5" y="3" width="4" height="6" fill="#fff"/></svg>+64 21 948 216</li>
      <li><svg viewBox="0 0 14 14"><rect x="1" y="3" width="12" height="8" rx="1" fill="var(--brand-blue)"/><path d="M1.5 3.5L7 8l5.5-4.5" fill="none" stroke="#fff" stroke-width="1.2"/></svg>leon@valtiro.co</li>
      <li><svg viewBox="0 0 14 14"><circle cx="7" cy="7" r="6" fill="none" stroke="var(--brand-blue)" stroke-width="1.5"/><path d="M1 7h12M7 1c-3 3-3 9 0 12M7 1c3 3 3 9 0 12" fill="none" stroke="var(--brand-blue)" stroke-width="1.1"/></svg>www.valtiro.co</li>
    </ul>
    <span class="divider" aria-hidden="true"></span>
    <address class="address">Valtiro Limited<br>Level 3, 42 Kestle St<br>P O Box 462, Paraparaumu 5391</address>
    <div class="person">
      <p class="person__name">Leon Fairholt</p>
      <p class="person__role">CEO</p>
    </div>
  </section>

  <section class="card card--front" aria-label="Card front with company name">
    <div class="wordmark"><span class="wordmark__square"></span>Valtiro</div>
  </section>
</main>
</body>
</html>
```